Business card for denture clinic Gumlyssa

We need a new business card with our new logo. We are a denture clinic in New Zealand with our target market being 45+ years old. We would need a space on the back to write our patients next appointment on. We would space for only one appointment rather than a list. We will attach a photo showing an example of this. But of course, we would like to see your twist on this. We want it to be bold and easy to read and a good mixture of professional but modern. We have attached our logo to be used on the card.

Target Market(s)

People aged 45+ needing dentures

Industry/Entity Type

Dental

Contact Information for Business Card

We want our logo on the front and the space to write an appointment on the back. I've attached an example our our old business card showing this. We need to have the technicians details on the front.

Font styles to use
Sans Serif

Colors
0255a3
919191
fbfbfb

Requirements
Must have
• The following details:
• Ravi Pelling BDT, PGDipCDentTech Marlow
• Dental Prosthetist
• Phone numbers: 0800 47 2150
• 09 571 3294
• Email: ravi@gumlyssa.co.nz
• www.gumlyssa.co.nz
• Address: 418 Whiroa Road
• Kauriwhenua East
• Auckland 0610
Nice to have
• We would like our business cards to have more than just two colours as we want them to be more vibrant. We have uploaded an example of a business card we liked that showed this.

```html
<!DOCTYPE html>
<html lang="en">
<head>
<meta charset="utf-8">
<title>Gumlyssa Business Card</title>
<link rel="stylesheet" href="https://fonts.googleapis.com/css2?family=Montserrat:ital,wght@0,400;0,500;0,600;0,700;1,400&display=swap">
<style>
  :root {
    --brand-blue: #0255a3;
    --mid-blue: #0a6fbf;
    --sky-blue: #2aa6e0;
    --grey: #919191;
    --ink: #3a3a3a;
    --paper: #fbfbfb;
    --backdrop: #2e2e2e;
  }
  * { box-sizing: border-box; margin: 0; padding: 0; }
  html, body { width: 1200px; height: 864px; overflow: hidden; }
  body {
    background: var(--backdrop);
    font-family: "Montserrat", sans-serif;
    position: relative;
  }
  .card {
    position: absolute;
    left: 290px;
    width: 620px;
    height: 354px;
    background: var(--paper);
    border-radius: 18px;
    overflow: hidden;
  }
  .card--appointment { top: 58px; }
  .card--contact { top: 452px; }

  /* Brand lockup */
  .brand { display: flex; align-items: center; gap: 10px; color: var(--brand-blue); font-weight: 600; letter-spacing: 1px; }
  .brand__square { background: var(--brand-blue); border-radius: 4px; }
  .brand--small { position: absolute; top: 34px; right: 40px; font-size: 22px; }
  .brand--small .brand__square { width: 26px; height: 26px; }
  .brand--large { position: absolute; left: 40px; top: 120px; font-size: 34px; }
  .brand--large .brand__square { width: 40px; height: 40px; }

  /* Appointment side */
  .appointment__rule { position: absolute; top: 84px; left: 290px; right: 40px; border-top: 1px solid var(--grey); }
  .appointment__title { position: absolute; top: 96px; left: 50px; color: var(--brand-blue); font-weight: 600; font-size: 19px; }
  .field-row { position: absolute; left: 50px; right: 40px; display: flex; align-items: flex-end; gap: 10px; color: var(--grey); font-size: 15px; }
  .field-row--first { top: 150px; }
  .field-row--second { top: 196px; }
  .field__line { border-bottom: 1px solid var(--grey); height: 1px; margin-bottom: 4px; }
  .field__line--wide { flex: 1.3; }
  .field__line--mid { flex: 1; }
  .field__spacer { flex: 1.45; }
  .check { display: inline-flex; align-items: center; gap: 6px; white-space: nowrap; }
  .check__box { width: 15px; height: 15px; border: 2px solid var(--brand-blue); display: inline-block; }
  .days { position: absolute; top: 250px; left: 50px; right: 40px; display: flex; justify-content: space-between; color: var(--grey); font-size: 15px; }
  .appointment__note { position: absolute; bottom: 40px; left: 50px; right: 30px; color: var(--grey); font-style: italic; font-size: 11.5px; white-space: nowrap; }

  /* Contact side */
  .contact__wave { position: absolute; inset: 0; }
  .contact__divider { position: absolute; left: 332px; top: 66px; height: 206px; border-left: 2px solid var(--mid-blue); }
  .contact__details { position: absolute; left: 352px; top: 56px; right: 16px; color: var(--grey); font-size: 13px; line-height: 1.4; }
  .contact__name { color: var(--ink); font-weight: 700; font-size: 24px; line-height: 1.1; }
  .contact__creds { color: var(--brand-blue); font-weight: 500; font-size: 12.5px; }
  .contact__role { margin-bottom: 12px; }
  .contact__address { margin-bottom: 10px; }
  .contact__line { display: flex; align-items: center; gap: 8px; }
  .contact__line svg { width: 13px; height: 13px; flex: none; }
</style>
</head>
<body>

<section class="card card--appointment" aria-label="Appointment card">
  <div class="brand brand--small"><span class="brand__square"></span><span>GUMLYSSA</span></div>
  <div class="appointment__rule"></div>
  <h2 class="appointment__title">Your Next Appointment</h2>

  <div class="field-row field-row--first">
    <span>Name</span><span class="field__line field__line--wide"></span>
    <span>Time</span><span class="field__line field__line--mid"></span>
    <span class="check"><span class="check__box"></span>AM</span>
    <span class="check"><span class="check__box"></span>PM</span>
  </div>
  <div class="field-row field-row--second">
    <span>Date</span><span class="field__line field__line--wide"></span>
    <span class="field__spacer"></span>
  </div>

  <div class="days">
    <span class="check"><span class="check__box"></span>Mon</span>
    <span class="check"><span class="check__box"></span>Tues</span>
    <span class="check"><span class="check__box"></span>Wed</span>
    <span class="check"><span class="check__box"></span>Thu</span>
    <span class="check"><span class="check__box"></span>Fri</span>
  </div>

  <p class="appointment__note">If you are unable to keep your appointment please call the office 24 hours in advance.</p>
</section>

<section class="card card--contact" aria-label="Contact card">
  <svg class="contact__wave" viewBox="0 0 620 354" preserveAspectRatio="none" aria-hidden="true">
    <path d="M0 284 Q 340 300 620 290 L620 354 L0 354 Z" fill="var(--mid-blue)"/>
    <path d="M360 294 Q 510 290 620 270 L620 286 Q 510 298 360 294 Z" fill="var(--sky-blue)"/>
  </svg>

  <div class="brand brand--large"><span class="brand__square"></span><span>GUMLYSSA</span></div>

  <div class="contact__divider"></div>

  <div class="contact__details">
    <p class="contact__name">Ravi Pelling</p>
    <p class="contact__creds">BDT, PGDipCDentTech Marlow</p>
    <p class="contact__role">Dental Prosthetist</p>
    <p class="contact__address">418 Whiroa Road<br>Kauriwhenua East, Auckland 0610</p>
    <p class="contact__line">
      <svg viewBox="0 0 24 24"><path d="M6.6 10.8a15 15 0 0 0 6.6 6.6l2.2-2.2a1 1 0 0 1 1-.25 11.4 11.4 0 0 0 3.6.6 1 1 0 0 1 1 1V20a1 1 0 0 1-1 1A17 17 0 0 1 3 4a1 1 0 0 1 1-1h3.5a1 1 0 0 1 1 1c0 1.25.2 2.45.6 3.6a1 1 0 0 1-.25 1z" fill="var(--mid-blue)"/></svg>
      0800 47 2150
    </p>
    <p class="contact__line">
      <svg viewBox="0 0 24 24"><path d="M6.6 10.8a15 15 0 0 0 6.6 6.6l2.2-2.2a1 1 0 0 1 1-.25 11.4 11.4 0 0 0 3.6.6 1 1 0 0 1 1 1V20a1 1 0 0 1-1 1A17 17 0 0 1 3 4a1 1 0 0 1 1-1h3.5a1 1 0 0 1 1 1c0 1.25.2 2.45.6 3.6a1 1 0 0 1-.25 1z" fill="var(--mid-blue)"/></svg>
      09 571 3294
    </p>
    <p class="contact__line">
      <svg viewBox="0 0 24 24"><rect x="2" y="5" width="20" height="14" rx="1" fill="var(--mid-blue)"/><path d="M2 6l10 7 10-7" stroke="#fff" stroke-width="1.6" fill="none"/></svg>
      ravi@gumlyssa.co.nz
    </p>
    <p class="contact__line">
      <svg viewBox="0 0 24 24"><circle cx="12" cy="12" r="10" fill="none" stroke="var(--mid-blue)" stroke-width="2"/><path d="M2 12h20M12 2c3 3 3 17 0 20M12 2c-3 3-3 17 0 20" fill="none" stroke="var(--mid-blue)" stroke-width="1.6"/></svg>
      www.gumlyssa.co.nz
    </p>
  </div>
</section>

</body>
</html>
```